Birch Flooring Supply

Basic one-sided business card design using the attached logo. Vintage americana theme. Font is modified Arial Nova Cond, but anything that coordinates can be used

```html
<!DOCTYPE html>
<html lang="en">
<head>
<meta charset="utf-8">
<title>Birch Flooring Supply – Business Card</title>
<link href="https://fonts.googleapis.com/css2?family=Roboto+Condensed:wght@400;700&display=swap" rel="stylesheet">
<style>
  :root {
    --stage: #c4c4c4;
    --card-dark: #121212;
    --card-mid: #262626;
    --gold: #c9a574;
    --gold-deep: #a98656;
    --ink-light: #ffffff;
  }
  html, body {
    margin: 0;
    width: 1200px;
    height: 1000px;
    overflow: hidden;
    background: var(--stage);
    font-family: "Roboto Condensed", "Arial Narrow", sans-serif;
  }
  .card {
    position: absolute;
    left: 75px;
    top: 200px;
    width: 1050px;
    height: 600px;
    border-radius: 24px;
    background: radial-gradient(ellipse at 45% 35%, var(--card-mid) 0%, var(--card-dark) 75%);
    overflow: hidden;
  }
  .brand {
    position: absolute;
    left: 40px;
    top: 278px;
    width: 430px;
    display: flex;
    align-items: center;
    justify-content: center;
    gap: 14px;
  }
  .brand-mark {
    flex: none;
    width: 22px;
    height: 22px;
    border-radius: 50%;
    background: var(--gold);
  }
  .brand-name {
    margin: 0;
    color: var(--gold);
    font-weight: 400;
    font-size: 30px;
    line-height: 44px;
  }
  .divider {
    position: absolute;
    left: 470px;
    top: 145px;
    height: 335px;
    border-left: 2px dashed var(--gold-deep);
  }
  .contact-block {
    position: absolute;
    left: 566px;
    top: 135px;
  }
  .person-name {
    margin: 0;
    color: var(--gold);
    font-weight: 700;
    font-size: 48px;
    line-height: 58px;
    letter-spacing: 1px;
  }
  .person-role {
    margin: 0;
    color: var(--ink-light);
    font-size: 26px;
    line-height: 30px;
  }
  .rule {
    width: 116px;
    height: 2px;
    background: var(--gold-deep);
    margin: 20px 0 28px;
  }
  .contact-list {
    list-style: none;
    margin: 0;
    padding: 0;
  }
  .contact-item {
    display: flex;
    align-items: flex-start;
    gap: 18px;
    color: var(--ink-light);
    font-size: 26px;
    line-height: 38px;
    margin-bottom: 6px;
  }
  .contact-item.address { margin-top: 10px; }
  .contact-icon {
    flex: none;
    width: 32px;
    height: 32px;
    margin-top: 3px;
  }
</style>
</head>
<body>
  <div class="card">
    <div class="brand">
      <span class="brand-mark" aria-hidden="true"></span>
      <p class="brand-name">Birch Flooring Supply</p>
    </div>

    <div class="divider"></div>

    <div class="contact-block">
      <h1 class="person-name">DANA HOLLIS</h1>
      <p class="person-role">Managing Director</p>
      <div class="rule"></div>
      <ul class="contact-list">
        <li class="contact-item">
          <svg class="contact-icon" viewBox="0 0 32 32" aria-hidden="true">
            <rect x="1.5" y="1.5" width="29" height="29" rx="4" fill="none" stroke="#c9a574" stroke-width="2"/>
            <path d="M10 9 l3 -1 2 5 -2 1.5 c1 2.5 2.5 4 5 5 l1.5 -2 5 2 -1 3 c-7 1 -14 -6 -13.5 -13.5z" fill="#c9a574"/>
          </svg>
          <span>044-555 010 222</span>
        </li>
        <li class="contact-item">
          <svg class="contact-icon" viewBox="0 0 32 32" aria-hidden="true">
            <rect x="1.5" y="1.5" width="29" height="29" rx="4" fill="none" stroke="#c9a574" stroke-width="2"/>
            <path d="M7 15 L24 8 L19 24 L15 18 Z" fill="#c9a574"/>
          </svg>
          <span>info@birchfloors.example</span>
        </li>
        <li class="contact-item">
          <svg class="contact-icon" viewBox="0 0 32 32" aria-hidden="true">
            <rect x="1.5" y="1.5" width="29" height="29" rx="4" fill="none" stroke="#c9a574" stroke-width="2"/>
            <circle cx="16" cy="16" r="8" fill="none" stroke="#c9a574" stroke-width="2"/>
            <path d="M8 16 H24 M16 8 C12 12 12 20 16 24 M16 8 C20 12 20 20 16 24" fill="none" stroke="#c9a574" stroke-width="1.5"/>
          </svg>
          <span>www.birchfloors.example</span>
        </li>
        <li class="contact-item address">
          <svg class="contact-icon" viewBox="0 0 32 32" aria-hidden="true">
            <rect x="1.5" y="1.5" width="29" height="29" rx="4" fill="none" stroke="#c9a574" stroke-width="2"/>
            <path d="M16 25 C11 19 10 16 10 13.5 A6 6 0 0 1 22 13.5 C22 16 21 19 16 25z" fill="none" stroke="#c9a574" stroke-width="2"/>
            <circle cx="16" cy="13.5" r="2.2" fill="#c9a574"/>
          </svg>
          <span>4410 Cypress Bay Blvd,<br>212-C, FL 32500</span>
        </li>
      </ul>
    </div>
  </div>
</body>
</html>
```